Flyer/Broschürre für Ambulanter Betreuungsdienst
Zielgruppe
Ambulanter Betreuungsdienst,Dienstleistungen für Senioren und Menschen mit Beeinträchtigung
Nach Paragraph 43b 45a/b & 53b SGBXI
Unterstützung im Alltag:
-Begleitung zu Arztbesuchen,Therapien &Terminbegleitung aller Art,
-Hilfe beim Einkaufen & Besorgungen + Transport
-Unterstützung bei der Tagesstrukturierung & Organisation im Alltag
-Erinnerungsservice zb. Einahme von Medikamenten ggbf. Kontrolle
-Begleitung zu Sportveranstaltungen,Theater uvm.
für zuverlässige Sicherheit und Orientierung.
-Gemeinsames Spazieren gehen ( Bewegungsangebote)
- Lesen & Vorlesen
-Gemeinsames Kochen und geselschaft leisten beim essen.
-Unterstützung bei Terminplanungen,Hilfe bei der komunikation mit Medizinischen Personal.
Soziale Betreuung & Aktivierung:
-Geselschaft leisten,Gespräche führen ;
-Freizeitaktivitäten Planen & Durchführen
-Gemeinsames Lesen und Vorlesen
-Karten & Brettspiele spielen
-Malen & Basteln
-Briefe schreiben,Emails verfassen
-Gemeinsam alte interessen wecken und neue finden.
-Angehörige entlasten
-kommunikation & Informationsaustausch über Fortschritte und Bedürfnisse
-Betreuung & Aktivierung für Menschen mit Demenz
-Erinnerungspflege,Biografie Arbeit
-Individuelle Betreuung
-Kurz und Langzeit Betreuung
-Nachtpflege
-Bewegungsangebote
-Spiele spielen zb. Brett & Gemeinschsftsspiele
Dienstleistungen Haushaltsbereich
-Reinigung von Böden(Saugen & Wischen)
-Reinigung Küche und Bad
-Bett frisch Beziehen
-Fenster Reinigung (innen & außen)
-Haustiere versorgen (mit dem Hund spazieren gehen)
-Wäsche waschen
-Dekorieren
-uvm
Aufgabenstellung
Freundliches Design , vertrauenswürdiges Erscheinungsbild mit warmen Farben.
Firmenname ( Sonnwerk) logo sollte einen Sonnwerk darstellen.
Slogan Text:
Verlässlichkeit und Fürsorge mit Herz & Verstand.
Format soll handlich und nicht zu klein sein,damit Senioren es gut lesen bzw erkennen können.

```html
<!DOCTYPE html>
<html lang="de">
<head>
<meta charset="utf-8">
<title>Sonnwerk – Ambulanter Betreuungsdienst</title>
<link href="https://fonts.googleapis.com/css2?family=Dancing+Script:wght@500;600&family=Ubuntu:wght@400;500;700&display=swap" rel="stylesheet">
<style>
  :root{
    --teal:#21b3b3;
    --white:#ffffff;
    --ink:#111111;
    --stage:#d9dcdc;
    --script:"Dancing Script", cursive;
    --sans:"Ubuntu", sans-serif;
  }
  *{box-sizing:border-box;margin:0;padding:0}
  html,body{width:1200px;height:1163px;overflow:hidden;background:var(--stage)}
  body{position:relative;font-family:var(--sans);color:var(--white)}
  .panel{position:absolute;background:var(--teal);overflow:hidden}
  .photo{position:absolute}
  ul.list{list-style:none}
  ul.list li{position:relative;padding-left:10px;margin-bottom:5px;line-height:1.12;font-weight:500}
  ul.list li::before{content:"";position:absolute;left:0;top:.5em;width:3px;height:3px;border-radius:50%;background:var(--white)}
  .script{font-family:var(--script);font-weight:500;line-height:1.05}
  .brand{position:absolute;display:flex;align-items:center;gap:7px}
  .brand-name{font-family:var(--sans);font-weight:700;color:var(--ink)}
  .brand-dot{display:block;border-radius:50%;background:var(--teal)}
  .arrow{position:absolute;width:0;height:0;border-top:7px solid transparent;border-bottom:7px solid transparent}

  /* Front cover */
  .cover{left:75px;top:90px;width:341px;height:489px}
  .cover-head{position:absolute;left:0;top:0;width:100%;height:95px;background:var(--white)}
  .cover-head .brand{left:82px;top:30px}
  .cover-head .brand-name{font-size:31px}
  .cover-head .brand-dot{width:18px;height:18px}
  .cover-photo{left:0;top:95px;width:341px;height:205px;
    background:radial-gradient(circle at 28% 35%,#fff6d8 0,#f4c873 14%,#8a6a3c 38%,#4e5a2e 62%,#34402a 100%);
    clip-path:polygon(0 0,100% 0,100% 100%,19% 100%)}
  .cover-slogan{position:absolute;left:0;top:312px;width:100%;text-align:center;font-size:20px}
  .cover-text{position:absolute;left:0;top:368px;width:100%;text-align:center;font-size:12px;line-height:1.18}
  .cover-text strong{font-weight:700}
  .cover-text p+p{margin-top:8px}

  /* Inside spread */
  .spread{position:absolute;left:75px;top:599px;width:687px;height:487px}
  .alltag{left:0;top:0;width:206px;height:487px}
  .alltag h2{position:absolute;left:38px;top:24px;font-size:25px}
  .alltag .list{position:absolute;left:28px;top:100px;width:168px;font-size:10.4px}
  .alltag .list li{margin-bottom:5.2px}

  .photo-column{position:absolute;left:206px;top:0;width:137px;height:487px;background:var(--white)}
  .photo-garden{left:0;top:0;width:137px;height:228px;background:linear-gradient(160deg,#5f8f3a 0%,#9cbf5e 45%,#6a8ab2 75%,#c9d2c4 100%)}
  .photo-portrait{left:0;top:228px;width:137px;height:127px;background:linear-gradient(140deg,#d9d2c6 0%,#b84a3a 45%,#3b3330 100%)}
  .demenz{position:absolute;left:12px;top:370px;width:112px;font-size:18px;color:var(--teal)}
  .demenz-arrow{left:118px;top:378px;border-left:9px solid var(--teal)}

  .soziale{left:343px;top:0;width:344px;height:487px}
  .photo-kitchen{left:0;top:0;width:344px;height:228px;
    background:linear-gradient(180deg,#8b8680 0%,#b9a79a 40%,#e3d7cf 70%,#f3f1ee 100%);
    clip-path:polygon(0 0,98.7% 0,79% 100%,0 100%)}
  .soziale .brand{left:110px;top:188px}
  .soziale .brand-name{font-size:24px}
  .soziale .brand-dot{width:14px;height:14px}
  .soziale h2{position:absolute;left:15px;top:240px;font-size:19.5px}
  .soziale-arrow{left:148px;top:253px;border-left:9px solid var(--white)}
  .soziale .list{position:absolute;font-size:10.2px}
  .list-right{left:168px;top:244px;width:150px}
  .list-left{left:14px;top:338px;width:125px}
  .list-right li,.list-left li{margin-bottom:4.6px}

  /* Back panel */
  .back{left:787px;top:599px;width:342px;height:487px}
  .back h2{position:absolute;left:39px;top:34px;font-size:24px}
  .back .list{position:absolute;left:37px;top:102px;width:300px;font-size:10.4px}
  .back .list li{margin-bottom:5.2px}
  .contact-card{position:absolute;left:0;top:277px;width:342px;height:210px;background:var(--white);
    clip-path:polygon(0 0,80.5% 0,100% 100%,0 100%);color:var(--ink)}
  .contact-card .brand{left:90px;top:22px}
  .contact-card .brand-name{font-size:24px}
  .contact-card .brand-dot{width:13px;height:13px}
  .tagline{position:absolute;left:90px;top:58px;width:190px;font-size:6px;line-height:1.25;font-weight:500}
  .contact{position:absolute;left:90px;list-style:none;color:var(--teal);font-weight:500}
  .contact li{display:flex;align-items:center;gap:7px}
  .contact svg{flex:none}
  .c-addr{top:93px;font-size:9.5px}
  .c-phone{top:114px;font-size:13.5px}
  .c-mail{top:140px;font-size:9.5px}
  .c-web{top:161px;font-size:9.5px}
</style>
</head>
<body>

<section class="panel cover">
  <div class="cover-head">
    <div class="brand"><span class="brand-name">Sonnwerk</span><span class="brand-dot"></span></div>
  </div>
  <div class="photo cover-photo" role="img" aria-label="Foto: Hände einer Betreuerin und einer Seniorin im Rollstuhl halten sich im Gegenlicht der Abendsonne"></div>
  <p class="cover-slogan script">„Verlässlichkeit und Fürsorge<br>mit Herz &amp; Verstand“</p>
  <div class="cover-text">
    <p><strong>Wir unterstützen Senioren und Menschen mit<br>Beeinträchtigung im Alltag –</strong><br>zuverlässig, herzlich und individuell.</p>
    <p>Ob Begleitung, Haushalt oder soziale Betreuung:<br><strong>Sonnwerk</strong> schafft Orientierung,<br>Entlastung und mehr Lebensqualität.</p>
  </div>
</section>

<section class="spread">
  <div class="panel alltag">
    <h2 class="script">Unterstützung<br>im Alltag</h2>
    <ul class="list">
      <li>Begleitung zu Arztbesuchen, Therapien und Terminbeglei­tungen aller Art</li>
      <li>Hilfe beim Einkaufen und bei Besorgungen + Transport</li>
      <li>Unterstützung bei der Tagesstrukturierung und Organisation im Alltag</li>
      <li>Erinnerungsservice, z. B. Einnahme von Medikamenten, ggf. Kontrolle</li>
      <li>Begleitung zu Sportveran­staltungen, Theater u. v. m. für zuverlässige Sicherheit und Orientierung</li>
      <li>Gemeinsame Spaziergänge (Bewegungsangebote)</li>
      <li>Lesen und Vorlesen</li>
      <li>Gemeinsames Kochen und Gesellschaft leisten beim Essen</li>
      <li>Unterstützung bei Terminplanungen, Hilfe bei der Kommunikation mit medizinischem Personal</li>
    </ul>
  </div>

  <div class="photo-column">
    <div class="photo photo-garden" role="img" aria-label="Foto: Betreuerin mit Seniorin im Rollstuhl auf einem Weg im Grünen"></div>
    <div class="photo photo-portrait" role="img" aria-label="Foto: lachender Senior im Rollstuhl mit seinem Hund"></div>
    <p class="demenz script">Betreuung &amp; Aktivierung für Menschen mit Demenz</p>
    <span class="arrow demenz-arrow"></span>
  </div>

  <div class="panel soziale">
    <div class="photo photo-kitchen" role="img" aria-label="Foto: zwei junge Frauen schneiden gemeinsam Obst in einer hellen Küche"></div>
    <div class="brand"><span class="brand-name">Sonnwerk</span><span class="brand-dot"></span></div>
    <h2 class="script">Soziale Betreuung<br>&amp; Aktivierung</h2>
    <span class="arrow soziale-arrow"></span>
    <ul class="list list-right">
      <li>Gesellschaft leisten, Gespräche führen</li>
      <li>Freizeitaktivitäten planen und durchführen</li>
      <li>Gemeinsames Lesen und Vorlesen</li>
      <li>Karten- und Brettspiele spielen</li>
      <li>Malen und Basteln</li>
      <li>Briefe schreiben, E-Mails verfassen</li>
      <li>Gemeinsam alte Interessen wecken und neue finden</li>
      <li>Angehörige entlasten</li>
      <li>Kommunikation und Informationsaustausch über Fortschritte und Bedürfnisse</li>
    </ul>
    <ul class="list list-left">
      <li>Erinnerungspflege, Biografiearbeit</li>
      <li>Individuelle Betreuung</li>
      <li>Kurz- und Langzeitbetreuung</li>
      <li>Nachtpflege</li>
      <li>Bewegungsangebote</li>
      <li>Spiele spielen, z. B. Brett- und Gemeinschaftsspiele</li>
    </ul>
  </div>
</section>

<section class="panel back">
  <h2 class="script">Dienstleistungen im<br>Haushaltsbereich</h2>
  <ul class="list">
    <li>Reinigung von Böden (Saugen und Wischen)</li>
    <li>Reinigung von Küche und Bad</li>
    <li>Bett frisch beziehen</li>
    <li>Fensterreinigung (innen und außen)</li>
    <li>Haustiere versorgen<br>(mit dem Hund spazieren gehen)</li>
    <li>Wäsche waschen</li>
    <li>Dekorieren</li>
    <li>u. v. m.</li>
  </ul>
  <div class="contact-card">
    <div class="brand"><span class="brand-name">Sonnwerk</span><span class="brand-dot"></span></div>
    <p class="tagline">Ambulanter Betreuungsdienst, Dienstleistungen<br>für Senioren und Menschen mit Beeinträchtigung<br>Nach Paragraph 43b 45a/b &amp; 53b SGBXI</p>
    <ul class="contact c-addr"><li>
      <svg width="10" height="13" viewBox="0 0 10 13"><path d="M5 0C2.2 0 0 2.2 0 5c0 3.6 5 8 5 8s5-4.4 5-8c0-2.8-2.2-5-5-5z" fill="#21b3b3"/><circle cx="5" cy="5" r="1.8" fill="#fff"/></svg>
      Lindenweg 7, 34567 Birkenfelde</li></ul>
    <ul class="contact c-phone"><li>
      <svg width="10" height="14" viewBox="0 0 10 14"><rect x="1" y="1" width="8" height="12" rx="1.5" fill="none" stroke="#21b3b3" stroke-width="1.2"/><circle cx="5" cy="10.5" r=".8" fill="#21b3b3"/></svg>
      +49 30 98 76 54 32</li></ul>
    <ul class="contact c-mail"><li>
      <svg width="11" height="8" viewBox="0 0 11 8"><rect width="11" height="8" rx="1" fill="#21b3b3"/><path d="M.5 .8 5.5 4.6 10.5 .8" fill="none" stroke="#fff" stroke-width="1"/></svg>
      info@sonnwerk.de</li></ul>
    <ul class="contact c-web"><li>
      <svg width="11" height="11" viewBox="0 0 11 11"><g fill="none" stroke="#21b3b3" stroke-width="1"><circle cx="5.5" cy="5.5" r="5"/><ellipse cx="5.5" cy="5.5" rx="2.2" ry="5"/><path d="M.5 5.5h10M1.3 3h8.4M1.3 8h8.4"/></g></svg>
      www.sonnwerk.de</li></ul>
  </div>
</section>

</body>
</html>
```